Bref créative
Karvelo ApS wants a cool new identity on stationary
Total outline for the stationary stuff
Simple
Henrik Dahlquist
CEO
Birkeslette 218
5810 Ravnsholt
Nordmark
henrik@karvelo.dk
www.karvelo.dk
Free your mind
We want the design to show trust, technology, to be frontrunner, inovation etc. - streamlined with a crisp look.

```html
<!DOCTYPE html>
<html lang="en">
<head>
<meta charset="utf-8">
<title>Karvelo ApS – Business Card</title>
<link href="https://fonts.googleapis.com/css2?family=Open+Sans:wght@400;600;700&display=swap" rel="stylesheet">
<style>
  :root {
    --backdrop: #3b3b3b;
    --card: #ffffff;
    --lime: #8cc63f;
    --charcoal: #3c3c3c;
    --ink: #4a4a4a;
    --rule: #cfcfcf;
  }
  html, body {
    margin: 0;
    padding: 0;
    width: 1200px;
    height: 965px;
    overflow: hidden;
    background: var(--backdrop);
    font-family: "Open Sans", Arial, sans-serif;
  }
  .business-card {
    position: absolute;
    left: 160px;
    top: 226px;
    width: 880px;
    height: 512px;
    border-radius: 24px;
    overflow: hidden;
    background: var(--card);
  }
  .card-swooshes {
    position: absolute;
    inset: 0;
  }
  .brand {
    position: absolute;
    left: 170px;
    top: 118px;
    display: flex;
    align-items: center;
    gap: 26px;
  }
  .brand-square {
    width: 64px;
    height: 64px;
    background: var(--lime);
    border-radius: 6px;
  }
  .brand-name {
    font-weight: 700;
    font-size: 86px;
    line-height: 1;
    color: var(--charcoal);
    letter-spacing: -1px;
  }
  .identity {
    position: absolute;
    right: 440px;
    top: 292px;
    text-align: right;
    color: var(--ink);
    white-space: nowrap;
  }
  .identity .person {
    font-size: 31px;
    font-weight: 700;
    color: var(--lime);
    line-height: 1.15;
  }
  .identity .role {
    font-size: 19px;
    font-weight: 600;
    margin-bottom: 12px;
  }
  .identity .address {
    font-size: 22px;
    line-height: 1.5;
  }
  .divider {
    position: absolute;
    left: 462px;
    top: 282px;
    width: 2px;
    height: 170px;
    background: var(--rule);
  }
  .contacts {
    position: absolute;
    left: 490px;
    top: 290px;
    margin: 0;
    padding: 0;
    list-style: none;
    color: var(--ink);
    font-size: 22px;
    line-height: 38px;
    white-space: nowrap;
  }
  .contacts li {
    display: flex;
    align-items: center;
    gap: 14px;
  }
  .contacts svg {
    width: 22px;
    height: 22px;
    flex: none;
  }
  .contacts .at-sign {
    width: 22px;
    text-align: center;
    font-weight: 700;
    color: var(--lime);
  }
</style>
</head>
<body>
  <section class="business-card">
    <svg class="card-swooshes" viewBox="0 0 880 512" width="880" height="512">
      <path d="M150,0 C85,65 35,170 0,330 L0,305 C30,160 72,60 128,0 Z" fill="var(--charcoal)"/>
      <path d="M0,0 L128,0 C72,60 30,160 0,305 Z" fill="var(--lime)"/>
      <path d="M880,8 C818,170 772,380 738,512 L762,512 C792,380 832,180 880,34 Z" fill="var(--charcoal)"/>
      <path d="M880,34 C832,180 792,380 762,512 L880,512 Z" fill="var(--lime)"/>
    </svg>

    <div class="brand">
      <span class="brand-square"></span>
      <span class="brand-name">Karvelo</span>
    </div>

    <div class="identity">
      <div class="person">Henrik Dahlquist</div>
      <div class="role">CEO</div>
      <div class="address">Birkeslette 218<br>5810 Ravnsholt, Nordmark</div>
    </div>

    <div class="divider"></div>

    <ul class="contacts">
      <li>
        <svg viewBox="0 0 24 24" aria-hidden="true"><path d="M6 3 L9 3 L11 8 L8.5 10 C9.8 12.8 11.2 14.2 14 15.5 L16 13 L21 15 L21 18 C21 19.5 19.5 21 18 21 C10 20.5 3.5 14 3 6 C3 4.5 4.5 3 6 3 Z" fill="var(--lime)"/></svg>
        +45 48207315
      </li>
      <li>
        <svg viewBox="0 0 24 24" aria-hidden="true"><rect x="6" y="2" width="12" height="20" rx="2" fill="var(--lime)"/><rect x="8" y="5" width="8" height="11" fill="#fff"/><circle cx="12" cy="19" r="1.2" fill="#fff"/></svg>
        +45 61394072
      </li>
      <li>
        <span class="at-sign">@</span>
        henrik@karvelo.dk
      </li>
      <li>
        <svg viewBox="0 0 24 24" aria-hidden="true"><g fill="none" stroke="var(--lime)" stroke-width="2"><circle cx="12" cy="12" r="9"/><ellipse cx="12" cy="12" rx="4" ry="9"/><path d="M3 12 H21"/></g></svg>
        www.karvelo.dk
      </li>
    </ul>
  </section>
</body>
</html>
```